rt for guide - bartholomew finch personal speaking/consulting website

custom website for my personal speaking/consulting services brand, you can see the basic site we are using as a placeholder at www.rtforguide.example now. I want to re-position this to more of a personal brand site and have video samples of speaking events, downloadable content, a video blog, and links to podcast. I really like the design of dorianwelk.example and the feature set should be fairly similar to his. I'll begin to compile more stock images etc. to use for sliders like he has done, for now we'll need to use stock imagery or existing photography from my social accounts. You can get a feel for social at all platforms/bfinchbroker i.e. facebook.com/bfinchbroker. the site should be primarily geared toward showcasing speaking/consulting services and content, as well as be flexible to allow for additional downloadables etc. in the future.

Target Market(s)

entrepreneurs and leaders looking to grow themselves, their business, and those they lead.

Coding

Coded - Design and coding required

Number of Pages Required

3 page

Font styles to use
Sans Serif

Colors

Designer to choose colors to be used in the design.

Requirements
Must have
• modern slick design, video blog, podcast feed, registration for people to subscribe to newsletter

```html
<!DOCTYPE html>
<html lang="en">
<head>
<meta charset="utf-8">
<title>RT for Guide — Bartholomew Finch</title>
<link rel="stylesheet" href="https://fonts.googleapis.com/css2?family=Oswald:wght@500;600;700&family=Open+Sans:ital,wght@0,400;0,600;1,400&family=Roboto+Condensed:wght@400;700&display=swap">
<style>
  :root{
    --navy:#2f3150;
    --orange:#e8582a;
    --orange-deep:#de5528;
    --ink:#1f2233;
    --body:#555a66;
    --mist:#dfe7ee;
    --paper:#f3f3f3;
    --white:#ffffff;
    --sky:#2f8fd8;
  }
  *{box-sizing:border-box;margin:0;padding:0}
  html,body{width:1200px;height:5094px;overflow:hidden}
  body{position:relative;background:var(--white);font-family:"Open Sans",sans-serif;color:var(--ink)}
  section,header,footer{position:absolute;left:0;width:1200px;overflow:hidden}
  .abs{position:absolute}
  .heading{font-family:"Oswald",sans-serif;font-weight:700;text-transform:uppercase;color:var(--ink);letter-spacing:.5px}
  .cond{font-family:"Roboto Condensed",sans-serif}
  .btn{position:absolute;display:flex;align-items:center;justify-content:center;background:var(--orange);color:var(--white);font-family:"Roboto Condensed",sans-serif;font-weight:700;font-size:18px;text-transform:uppercase;border-radius:4px;letter-spacing:.5px}
  .photo{position:absolute}
  .play{position:absolute;width:60px;height:42px;border-radius:10px;background:#e62117;display:flex;align-items:center;justify-content:center}
  .play::after{content:"";border-left:18px solid #fff;border-top:11px solid transparent;border-bottom:11px solid transparent;margin-left:4px}

  /* Hero */
  .hero{top:0;height:676px}
  .hero-bg{inset:0;background:linear-gradient(100deg,#e9eef3 0%,#cfd9e2 45%,#aebccb 70%,#3b4a6a 100%)}
  .brand{left:75px;top:22px;font-family:"Roboto Condensed",sans-serif;font-weight:700;font-size:44px;color:var(--ink)}
  .nav{right:86px;top:30px;display:flex;gap:30px;align-items:center;font-size:14px;color:#3a3d4a;text-transform:uppercase}
  .nav .active{color:var(--orange);border:1.5px solid var(--orange);border-radius:50%;width:56px;height:56px;display:flex;align-items:center;justify-content:center;margin-right:-6px}
  .hero-title{left:142px;top:236px;font-family:"Oswald",sans-serif;font-weight:700;font-size:74px;line-height:78px;color:#2b2e3e}
  .hero-sub{left:158px;top:404px;font-style:italic;font-size:17px;line-height:28px;color:#3b3f4d}
  .hero-play{left:346px;top:544px;width:64px;height:64px;border-radius:50%;border:3px solid var(--orange);display:flex;align-items:center;justify-content:center}
  .hero-play::after{content:"";border-left:22px solid var(--orange);border-top:14px solid transparent;border-bottom:14px solid transparent;margin-left:6px}

  /* Newsletter */
  .newsletter{top:676px;height:174px;background:var(--navy)}
  .newsletter h2{left:299px;top:24px;font-family:"Oswald",sans-serif;font-weight:500;font-size:28px;color:#fff}
  .newsletter p{left:300px;top:66px;font-size:12px;color:#e4e6ef}
  .field{position:absolute;top:101px;height:40px;background:#fff;border-radius:3px;font-size:11px;color:#aaa;padding:12px 14px}

  /* About */
  .about{top:850px;height:593px;background:linear-gradient(var(--mist) 0 469px,var(--paper) 469px)}
  .about-title{right:799px;top:60px;text-align:right}
  .about-title h2{font-size:44px;line-height:52px}
  .about-title span{font-size:22px;font-weight:700;color:var(--ink)}
  .about-copy{left:490px;top:68px;width:580px}
  .about-copy h3{font-size:15px;font-weight:600;margin-bottom:14px}
  .about-copy p{font-size:12px;line-height:29px;color:var(--body);margin-bottom:10px}
  .about-copy .accent{color:var(--orange)}
  .read{font-family:"Roboto Condensed",sans-serif;font-weight:700;font-size:13px;color:var(--orange);text-transform:uppercase}

  /* Blog */
  .blog{top:1443px;height:712px;background:#fff;text-align:center}
  .section-title{width:1200px;left:0;font-size:48px;text-align:center}
  .blog .lede{left:0;width:1200px;top:122px;font-size:15px;font-weight:600;text-align:center}
  .post{position:absolute;top:192px;width:510px;text-align:center}
  .post .photo{position:relative;width:510px;height:281px}
  .post .kicker{margin-top:20px;font-size:14px;color:var(--orange)}
  .post .text{margin-top:18px;font-family:"Roboto Condensed",sans-serif;font-weight:700;font-size:17px;line-height:26px;color:var(--ink)}

  /* Video post */
  .video{top:2155px;height:658px;background:var(--paper)}
  .video-card{left:138px;top:118px;width:534px;height:416px;background:#fff}
  .video-card h2{position:absolute;left:52px;top:104px;font-size:48px}
  .kicker-o{font-size:14px;color:var(--orange)}

  /* Podcasts */
  .podcasts{top:2813px;height:574px;background:var(--navy);color:#fff}
  .podcasts h2{left:666px;top:72px;font-size:50px;color:#fff}
  .podcasts .p-sub{left:670px;top:140px;font-size:15px;color:#e4e6ef}
  .podcasts h3{left:664px;top:205px;width:440px;font-family:"Roboto Condensed",sans-serif;font-size:21px;line-height:29px}
  .podcasts .p-body{left:664px;top:278px;width:470px;font-size:12px;line-height:29px;color:#d5d8e4}
  .round-play{position:absolute;width:64px;height:64px;border-radius:50%;background:rgba(255,255,255,.75);border:2px solid #333;display:flex;align-items:center;justify-content:center}
  .round-play::after{content:"";border-left:18px solid #333;border-top:11px solid transparent;border-bottom:11px solid transparent;margin-left:6px}

  /* Events */
  .events{top:3387px;height:488px;background:#fff}
  .event{position:absolute;top:152px;width:245px;height:267px;background:#fff;box-shadow:0 2px 8px rgba(0,0,0,.12)}
  .event .photo{position:relative;width:245px;height:190px}
  .event .mini-play{position:absolute;right:12px;top:152px;width:30px;height:30px;border-radius:50%;background:rgba(255,255,255,.85);border:1.5px solid #222}
  .event .mini-play::after{content:"";position:absolute;left:11px;top:8px;border-left:9px solid #222;border-top:6px solid transparent;border-bottom:6px solid transparent}
  .event h4{margin:16px 0 0 14px;font-family:"Roboto Condensed",sans-serif;font-size:15px;text-transform:uppercase}
  .event a{display:block;margin:6px 0 0 14px;font-size:12px;color:var(--orange);text-decoration:none}

  /* CTA */
  .cta{top:3875px;height:253px;background:var(--orange-deep);color:#fff}
  .cta h2{left:154px;top:60px;font-size:48px;color:#fff}
  .cta p{left:154px;top:135px;width:620px;font-size:13px;line-height:28px}
  .outline{position:absolute;left:815px;top:105px;width:199px;height:50px;border:2px solid #fff;border-radius:4px;display:flex;align-items:center;justify-content:center;font-family:"Roboto Condensed",sans-serif;font-weight:700;font-size:18px;text-transform:uppercase}

  /* Follow */
  .follow{top:4128px;height:567px;background:#f6f6f7}
  .follow h2{left:109px;top:150px;font-size:48px;line-height:56px}
  .follow h2 .tag{color:var(--orange);text-transform:none}
  .grid{left:540px;top:79px;display:grid;grid-template-columns:repeat(3,188px);grid-auto-rows:168px;gap:10px 10px}

  /* Footer */
  .footer{top:4695px;height:399px;background:var(--navy);text-align:center;color:#fff}
  .footer .f-brand{width:1200px;left:0;top:50px;font-family:"Roboto Condensed",sans-serif;font-weight:700;font-size:44px;color:#fff}
  .footer h3{width:1200px;left:0;top:132px;font-family:"Oswald",sans-serif;font-weight:500;font-size:32px;color:var(--orange)}
  .socials{left:448px;top:190px;display:flex;gap:10px}
  .social{width:44px;height:44px;border-radius:50%;background:var(--sky);border:2px solid #fff}
  .social.alt{background:var(--orange)}
  .f-links{width:1200px;left:0;top:278px;font-size:13px;color:#dfe1ea}
  .f-copy{width:1200px;left:0;top:304px;font-size:13px;color:#dfe1ea}
  .f-copy b{color:var(--orange);font-weight:400}
</style>
</head>
<body>

<header class="hero">
  <div class="abs hero-bg" role="img" aria-label="Smiling speaker in a checked shirt in front of a misty mountain landscape"></div>
  <div class="abs brand">RT for Guide</div>
  <nav class="abs nav">
    <span class="active">Home</span><span>About</span><span>Blog</span><span>Podcast</span><span>Events</span><span>Contact</span>
    <svg width="14" height="14" viewBox="0 0 14 14"><circle cx="5.5" cy="5.5" r="4.3" fill="none" stroke="#3a3d4a" stroke-width="1.5"/><line x1="8.6" y1="8.6" x2="13" y2="13" stroke="#3a3d4a" stroke-width="1.6"/></svg>
  </nav>
  <h1 class="abs hero-title">Transform<br>Your Life</h1>
  <p class="abs hero-sub">Decades Of Experience. Millions Of Lives<br>Changed. Undeniable Results.</p>
  <div class="abs hero-play" aria-label="Play intro video"></div>
</header>

<section class="newsletter">
  <div class="photo" style="left:118px;top:4px;width:149px;height:170px;background:linear-gradient(160deg,#f4f4f6,#c9ccd6 60%,#e8b89c)" role="img" aria-label="Hand holding a tablet showing a mail icon"></div>
  <h2 class="abs">Join Our Newsletter</h2>
  <p class="abs">Do you want to know about our blog post and update for Sign up for our newsletter!</p>
  <div class="field" style="left:300px;width:271px">Name *</div>
  <div class="field" style="left:583px;width:271px">Email *</div>
  <div class="btn" style="left:864px;top:101px;width:168px;height:40px;font-size:16px">Subscribe</div>
</section>

<section class="about">
  <div class="abs about-title">
    <h2 class="heading">About Us</h2>
    <span class="cond">Rt for Guide</span>
  </div>
  <div class="photo" style="left:117px;top:239px;width:306px;height:354px;background:linear-gradient(160deg,#4b6a8f,#1f3048 60%,#15161c)" role="img" aria-label="Portrait of Bartholomew Finch in a suit before glass office towers"></div>
  <div class="abs about-copy">
    <h3>lorem ipsum It was popularised in the with the release .</h3>
    <p>Lorem Ipsum is simply dummy text of the printing and typesetting industry. Lorem Ipsum has been the industry's standard dummy text ever since the 1500s, when an unknown printer took Lorem Ipsum is simply dummy text of the printing and typesetting industry. Lorem Ipsum has been the industry's standard dummy text ever since the 1500s, when an unknown printer took a galley of type and scrambled it to make a type specimen book. It has survived not only five centuries, but also the leap into electronic typesetting, remaining essentially unchanged.</p>
    <h3 style="margin-bottom:6px">lorem ipsum It was popu<span class="accent">larised in the with the release .</span></h3>
    <span class="read">Read More</span>
  </div>
</section>

<section class="blog">
  <h2 class="abs heading section-title" style="top:58px">Blog Post</h2>
  <p class="abs lede">Lorem Ipsum is simply dummy text of the printing and typesetting.</p>
  <article class="post" style="left:79px">
    <div class="photo" style="background:linear-gradient(120deg,#a7a396,#7d7a70 50%,#c9c7c0)" role="img" aria-label="Video still of the speaker in a blue polo in an office"><div class="play" style="left:225px;top:120px"></div></div>
    <p class="kicker">Lorem Ipsum has been the industry.</p>
    <p class="text">Lorem Ipsum is simply dummy text of the printing and<br>typesetting industry Lorem</p>
    <div class="btn" style="left:176px;top:409px;width:170px;height:50px">Watch Now</div>
  </article>
  <article class="post" style="left:611px">
    <div class="photo" style="background:linear-gradient(120deg,#d6d9d6,#b9bcba 55%,#3d4047)" role="img" aria-label="Video still of the speaker in a suit beside a whiteboard"><div class="play" style="left:215px;top:120px"></div></div>
    <p class="kicker">Lorem Ipsum has been the industry.</p>
    <p class="text">Lorem Ipsum is simply dummy text of the printing and<br>typesetting industry Lorem</p>
    <div class="btn" style="left:174px;top:409px;width:170px;height:50px">Watch Now</div>
  </article>
</section>

<section class="video">
  <div class="abs video-card">
    <h2 class="heading">Video Post</h2>
    <p class="abs kicker-o" style="left:54px;top:172px">Lorem Ipsum has been the industry.</p>
    <p class="abs cond" style="left:54px;top:198px;width:440px;font-weight:700;font-size:17px;line-height:28px">Lorem Ipsum is simply dummy text of the printing and typesetting industry Lorem</p>
    <div class="btn" style="left:54px;top:273px;width:172px;height:50px">Watch Now</div>
  </div>
  <div class="photo" style="left:676px;top:69px;width:386px;height:520px;background:linear-gradient(180deg,#2d4566,#8c7f8a 35%,#d69a5a 50%,#5d6a55 70%,#3f5a34)" role="img" aria-label="Video still of a marina at sunset with a cornhole board on the lawn"><div class="play" style="left:163px;top:240px"></div></div>
</section>

<section class="podcasts">
  <div class="photo" style="left:0;top:0;width:599px;height:574px;background:linear-gradient(110deg,#c7b7a4,#e3cf9a 45%,#7f9a68 80%,#4d5d74)" role="img" aria-label="Woman and girl with painted faces smiling at an outdoor event"><div class="round-play" style="left:502px;top:476px"></div></div>
  <h2 class="abs heading">Featured Podcasts</h2>
  <p class="abs p-sub">Ready for more? Listen to the latest podcast episode.</p>
  <h3 class="abs">Lorem Ipsum is simply dummy text of the printing and typesetting industry.</h3>
  <p class="abs p-body">Lorem Ipsum is simply dummy text of the printing and typesetting industry. Lorem Ipsum has been the industry's standard dummy text ever since the 1500s, when an unknown printer took Lorem Ipsum is simply dummy text of the printing and type.</p>
  <div class="btn" style="left:664px;top:421px;width:243px;height:48px">View More Podcasts</div>
</section>

<section class="events">
  <h2 class="abs heading section-title" style="top:50px">Speaking Events</h2>
  <div class="event" style="left:79px"><div class="photo" style="background:linear-gradient(120deg,#cfc9bd,#7a7d86)" role="img" aria-label="Speaker in a blue polo recording a video"></div><span class="mini-play"></span><h4>Lorem Ipsum Simple Text</h4><a>Read More...</a></div>
  <div class="event" style="left:344px"><div class="photo" style="background:linear-gradient(120deg,#d8d6d0,#b34a45)" role="img" aria-label="Speaker in a red polo recording a video"></div><span class="mini-play"></span><h4>Lorem Ipsum Simple Text</h4><a>Read More...</a></div>
  <div class="event" style="left:610px"><div class="photo" style="background:linear-gradient(120deg,#e9e8e6,#8d7c86)" role="img" aria-label="Speaker in a white shirt recording a video"></div><span class="mini-play"></span><h4>Lorem Ipsum Simple Text</h4><a>Read More...</a></div>
  <div class="event" style="left:876px"><div class="photo" style="background:linear-gradient(120deg,#8b8e93,#25262b)" role="img" aria-label="Speaker in a black shirt recording a video"></div><span class="mini-play"></span><h4>Lorem Ipsum Simple Text</h4><a>Read More...</a></div>
</section>

<section class="cta">
  <h2 class="abs heading">RT for Guide</h2>
  <p class="abs">Lorem Ipsum is simply dummy text of the printing and typesetting industry. Lorem Ipsum has been the industry's standard</p>
  <div class="outline">Download Now</div>
</section>

<section class="follow">
  <h2 class="abs heading">Follow Us On<br><span class="tag">#rtforguide</span></h2>
  <div class="abs grid">
    <div style="background:linear-gradient(160deg,#b9c6d4,#3c3f48)" role="img" aria-label="Event mascot at a parade"></div>
    <div style="background:linear-gradient(160deg,#4b2a6e,#6a3f8f)" role="img" aria-label="Purple event announcement poster"></div>
    <div style="background:linear-gradient(180deg,#3b4a66,#d3975a 55%,#48603a)" role="img" aria-label="Marina at sunset"></div>
    <div style="background:linear-gradient(160deg,#e4e1dc,#3a3b40)" role="img" aria-label="Group photo at a conference"></div>
    <div style="background:linear-gradient(160deg,#d8c4a0,#8da06f)" role="img" aria-label="Woman and girl with painted faces"></div>
    <div style="background:linear-gradient(160deg,#8b95a8,#4a3b3a)" role="img" aria-label="Speaker on stage addressing a crowd"></div>
  </div>
  <div class="btn" style="left:540px;top:445px;width:170px;height:49px">Follow Us</div>
</section>

<footer class="footer">
  <div class="abs f-brand">RT for Guide</div>
  <h3 class="abs">Submit A Question For Us Here.</h3>
  <div class="abs socials">
    <span class="social" role="img" aria-label="Social profile link 1"></span>
    <span class="social" role="img" aria-label="Social profile link 2"></span>
    <span class="social alt" role="img" aria-label="Social profile link 3"></span>
    <span class="social" role="img" aria-label="Social profile link 4"></span>
    <span class="social" role="img" aria-label="Social profile link 5"></span>
    <span class="social alt" role="img" aria-label="Social profile link 6"></span>
  </div>
  <p class="abs f-links">Home &nbsp;|&nbsp; About &nbsp;|&nbsp; Blog &nbsp;|&nbsp; Podcast &nbsp;|&nbsp; Events &nbsp;|&nbsp; Contact</p>
  <p class="abs f-copy">©<b>RT for Guide</b> - 2019 All Rights Reserved.</p>
</footer>

</body>
</html>
```